This is a label for a new sake made in Japan imported into Aust

This will be a bottle label for a new sake imported into Australia. The hero of the label is the Velmora. We have joined the "O" meaning great in Japanese and used sake with "Z" to have Velmora with the play on words using Oz as in our slang for Aussie. A modern label with a Japanese take is key. This is a premium sake made in Japan for the Australian market.
The "Tall Casks" up the top is the name of the company, we have yet to design a logo for the company.

Target Market(s)

Alcohol

Logo Text

Velmora

Font styles to use
Serif

Requirements
Must have
• easy to read, with a hint of Japanese origin
Should not have
• too busy

```html
<!DOCTYPE html>
<html lang="en">
<head>
<meta charset="utf-8">
<title>Velmora Premium Japanese Sake – Label</title>
<link rel="stylesheet" href="https://fonts.googleapis.com/css2?family=Montserrat:wght@300&family=Playfair+Display:wght@700;900&display=swap">
<style>
  :root {
    --paper: #ffffff;
    --stage: #ffffff;
    --blush: #e9b39c;
    --blush-deep: #dd9a86;
    --apricot: #f2b56e;
    --apricot-soft: #f7cf9c;
    --peach: #f6d3ab;
    --stone: #c9cdcb;
    --sun-red: #ec1c24;
    --ink-navy: #0d3a4f;
    --text-white: #ffffff;
  }
  html, body {
    margin: 0;
    padding: 0;
    width: 1200px;
    height: 848px;
    overflow: hidden;
    background: var(--stage);
  }
  .canvas {
    position: relative;
    width: 1200px;
    height: 848px;
  }
  .label {
    position: absolute;
    left: 267px;
    top: 44px;
    width: 666px;
    height: 760px;
    border: 1px solid #444;
    background: var(--paper);
    overflow: hidden;
  }
  .label svg { display: block; width: 100%; height: 100%; }
  .brand-name {
    font-family: "Playfair Display", Georgia, serif;
    font-weight: 900;
    fill: var(--ink-navy);
  }
  .tagline {
    font-family: "Montserrat", Arial, sans-serif;
    font-weight: 300;
    fill: var(--text-white);
    letter-spacing: 7px;
  }
  .company-name {
    font-family: "Playfair Display", Georgia, serif;
    font-weight: 700;
    fill: var(--ink-navy);
    letter-spacing: 14px;
  }
</style>
</head>
<body>
<main class="canvas">
  <section class="label" aria-label="Velmora sake bottle label">
    <svg viewBox="0 0 865 987" xmlns="http://www.w3.org/2000/svg">
      <g class="colour-blocks" role="img" aria-label="Soft watercolour blocks in blush, apricot, peach and stone">
        <rect class="block-blush-top" x="110" y="0" width="755" height="190" fill="var(--blush)" opacity="0.8"/>
        <path class="block-apricot-left" d="M0 0 H150 V180 H180 A120 195 0 0 1 180 570 H0 Z" fill="var(--apricot)" opacity="0.75"/>
        <rect class="block-stone-right" x="635" y="212" width="230" height="450" rx="18" fill="var(--stone)" opacity="0.85"/>
        <path class="block-peach-bottom" d="M300 987 C300 800 380 690 470 690 H865 V987 Z" fill="var(--peach)" opacity="0.85"/>
        <rect class="block-apricot-right" x="625" y="640" width="240" height="347" fill="var(--apricot-soft)" opacity="0.85"/>
        <path class="block-blush-left" d="M0 645 H165 Q185 645 185 670 V987 H0 Z" fill="var(--blush-deep)" opacity="0.8"/>
      </g>
      <circle class="rising-sun" cx="432" cy="492" r="267" fill="var(--sun-red)" opacity="0.97"/>
      <text class="brand-name" x="432" y="540" text-anchor="middle" font-size="128" textLength="620" lengthAdjust="spacingAndGlyphs">VELMORA</text>
      <text class="tagline" x="432" y="626" text-anchor="middle" font-size="24">PREMIUM</text>
      <text class="tagline" x="432" y="658" text-anchor="middle" font-size="24">JAPANESE SAKE</text>
      <text class="company-name" x="432" y="905" text-anchor="middle" font-size="42">TALLCASKS</text>
    </svg>
  </section>
</main>
</body>
</html>
```